Brindle Structures Construction Company Seeking Modern Website

We are a small construction company wanting to create a web presence. We don't have much in the way of current content but will get photos as they come in. Attached is a picture of our business card.
The pages we would like on the menu are:
Home
Portfolio
Product Specs
Testimonials
Our Process
Contact
Some designs we like are:
http://www.tovenquarnsheds.example/
http://www.qzrsheds.example/
http://pannowsheds.example/
http://wistenhalls.example/
Not much requirements other than that so feel free to be creative!
Updates
Target Market(s)
Construction
Commercial and Residential Buildings
Industry/Entity Type
Construction Company
Number of Pages Required
5+ page
Look and feel

```html
<!DOCTYPE html>
<html lang="en">
<head>
<meta charset="utf-8">
<title>Brindle Structures</title>
<link rel="stylesheet" href="https://fonts.googleapis.com/css2?family=Open+Sans:wght@400;600;700&family=Roboto:wght@400;500;700&display=swap">
<style>
:root{
  --red:#d32f27;
  --red-band:#c9302a;
  --blue:#0a9ad6;
  --blue-panel:rgba(8,140,205,.88);
  --heading-blue:#1b9bd7;
  --dark:#1c1c1c;
  --darker:#151515;
  --topbar:#f4f4f4;
  --grey-section:#f1f1f1;
  --text:#444;
  --muted:#777;
  --white:#fff;
}
*{box-sizing:border-box;margin:0;padding:0}
html,body{width:1200px;height:2483px;overflow:hidden}
body{position:relative;font-family:"Open Sans",Arial,sans-serif;color:var(--text);background:var(--white)}
.abs{position:absolute}
svg{display:block}

/* top bar */
.topbar{left:0;top:0;width:1200px;height:45px;background:var(--topbar);border-bottom:1px solid #e6e6e6}
.topbar .phone{left:58px;top:12px;font-size:13px;font-weight:600;color:#555;display:flex;align-items:center;gap:12px}
.topbar .mail{left:790px;top:12px;font-size:13px;color:#555;display:flex;align-items:center;gap:12px}
.social{display:flex;gap:10px}
.social span{width:24px;height:24px;border:1px solid #ccc;background:#fff;display:block}
.social span.active{border-color:var(--red)}
.topbar .social{left:1052px;top:10px}

/* header */
.header{left:0;top:45px;width:1200px;height:116px;background:#fff}
.brand{left:48px;top:16px;width:152px;height:88px;display:flex;align-items:center;gap:8px}
.brand i{width:14px;height:14px;background:var(--red);display:block}
.brand b{font-family:"Roboto",sans-serif;font-weight:700;font-size:17px;color:var(--red);line-height:1.1}
.nav{left:306px;top:49px;display:flex;gap:0;font-size:11.5px;font-family:"Open Sans",sans-serif}
.nav a{color:var(--heading-blue);text-decoration:none;text-transform:uppercase;position:absolute;white-space:nowrap}
.nav a.current{color:var(--red)}
.nav a.current::after{content:"";position:absolute;left:-4px;right:-4px;top:24px;height:2px;background:var(--red)}

/* hero */
.hero{left:0;top:161px;width:1200px;height:551px;background:linear-gradient(90deg,#a9c3d6 0%,#7d98ad 25%,#3b434c 50%,#24272c 75%,#2b2e33 100%)}
.hero-panel{left:536px;top:348px;width:616px;height:284px;background:var(--blue-panel);color:#fff;text-align:right;padding:48px 32px 0 40px}
.hero-panel h1{font-family:"Roboto",sans-serif;font-weight:500;font-size:40px;line-height:1;text-transform:uppercase;letter-spacing:.3px}
.hero-panel p{font-size:13.5px;font-weight:600;line-height:20px;margin-top:20px;padding-left:40px}
.btn-light{display:inline-block;background:#fff;color:var(--red);font-size:13px;padding:12px 27px;margin-top:23px;text-transform:uppercase}

/* login */
.login{left:0;top:712px;width:1200px;height:89px;background:var(--dark)}
.login label{position:absolute;color:#fff;font-size:21px;font-family:"Open Sans",sans-serif}
.login .field{position:absolute;height:37px;border:1px solid #555;background:#222;color:#999;font-size:10px;padding:11px 10px}
.login .forgot{position:absolute;left:522px;top:65px;font-size:10px;color:#ddd}
.login .submit{position:absolute;left:826px;top:22px;width:166px;height:46px;background:var(--red-band);color:#fff;font-size:11.5px;display:flex;align-items:center;justify-content:center;gap:10px}

/* welcome */
.welcome{left:45px;top:866px;width:580px}
.section-title{font-family:"Roboto",sans-serif;font-size:26px;font-weight:400;color:var(--heading-blue);text-transform:uppercase;line-height:1}
.section-title strong{font-weight:500}
.welcome p{font-size:12px;line-height:27px;color:#555;margin-top:18px;text-align:justify}
.btn-red{display:inline-block;background:var(--red-band);color:#fff;font-size:12px;padding:11px 22px;text-transform:uppercase;margin-top:21px}

.feed{left:678px;top:862px;width:476px}
.feed .view-all{position:absolute;right:2px;top:20px;font-size:11.5px;color:var(--red)}
.feed-item{display:flex;gap:15px;margin-top:16px;padding-bottom:8px;border-bottom:1px dotted #999}
.feed-item:first-of-type{margin-top:26px}
.feed-thumb{width:102px;height:80px;flex:none}
.feed-item time{font-size:11px;color:#999;display:block}
.feed-item h3{font-family:"Roboto",sans-serif;font-size:16px;font-weight:500;color:#222;margin-top:2px}
.feed-item p{font-size:11px;line-height:17px;color:#555;margin-top:2px}

/* projects */
.projects{left:0;top:1153px;width:1200px;height:916px;background:var(--grey-section)}
.tile{position:absolute;display:flex;flex-direction:column;align-items:center;justify-content:center;text-align:center;color:#fff}
.tile h2{font-family:"Roboto",sans-serif;font-weight:500;font-size:28px;line-height:30px;text-transform:uppercase;text-shadow:0 1px 3px rgba(0,0,0,.45)}
.tile p{font-size:13px;font-weight:600;line-height:20px;margin-top:20px;max-width:540px}
.tile .btn-red{padding:10px 24px;margin-top:14px;font-size:11.5px}

/* partners */
.partners{left:0;top:2069px;width:1200px;height:165px;background:var(--red-band)}
.partner{position:absolute;top:30px;width:294px;height:109px;border:8px solid rgba(255,255,255,.35);display:flex;align-items:center;justify-content:center}
.partner i{display:block;width:152px;height:46px;background:#fff}

/* contact */
.contact{left:0;top:2234px;width:1200px;height:154px;background:var(--darker)}
.contact-item{position:absolute;display:flex;align-items:center;gap:22px;color:#fff;font-size:19px;font-family:"Open Sans",sans-serif}
.contact-item.small{font-size:16px}
.icon-box{width:36px;height:36px;border:1px solid #3a3a3a;display:flex;align-items:center;justify-content:center}

/* footer */
.footer{left:0;top:2388px;width:1200px;height:95px;background:var(--blue)}
.footer .copy{position:absolute;left:0;width:1200px;top:38px;text-align:center;color:#fff;font-size:11.5px}
.footer .social{position:absolute;left:1036px;top:34px}
.footer .social span{border:none;width:28px;height:28px}
</style>
</head>
<body>

<div class="abs topbar">
  <div class="abs phone">
    <svg width="16" height="16" viewBox="0 0 24 24"><path fill="#d32f27" d="M6.6 10.8a15 15 0 006.6 6.6l2.2-2.2c.3-.3.7-.4 1-.2 1.1.4 2.3.6 3.6.6.6 0 1 .4 1 1V20c0 .6-.4 1-1 1A17 17 0 013 4c0-.6.4-1 1-1h3.5c.6 0 1 .4 1 1 0 1.3.2 2.5.6 3.6.1.3 0 .7-.2 1z"/></svg>
    1800 123 4567
  </div>
  <div class="abs mail">
    <svg width="14" height="12" viewBox="0 0 14 12"><rect x=".7" y=".7" width="12.6" height="10.6" fill="none" stroke="#d32f27" stroke-width="1.4"/><path d="M1 1l6 5 6-5" fill="none" stroke="#d32f27" stroke-width="1.4"/></svg>
    info@companyname.com
  </div>
  <div class="abs social"><span class="active"></span><span></span><span></span></div>
</div>

<header class="abs header">
  <div class="abs brand"><i></i><b>Brindle Structures</b></div>
  <nav class="abs nav">
    <a class="current" style="left:0">Home</a>
    <a style="left:85px">Portfolio</a>
    <a style="left:193px">Product Specs</a>
    <a style="left:330px">Testimonials</a>
    <a style="left:457px">Our Process</a>
    <a style="left:581px">Contact</a>
  </nav>
</header>

<section class="abs hero" role="img" aria-label="Businessman in a suit holding a glowing house outline above his open hand"></section>
<div class="abs hero-panel">
  <h1>Consectetur Adipiscing</h1>
  <p>Lorem ipsum dolor sit amet, consectetur adipiscing elit, sed do eiusmod tempor incididunt ut labore et dolore magna aliqua. Ut enim ad minim veniam, quis nostrud exercitation ullamco</p>
  <span class="btn-light">Read More</span>
</div>

<section class="abs login">
  <label style="left:68px;top:30px">Email :</label>
  <div class="field" style="left:145px;top:24px;width:225px">Enter Your Email id</div>
  <label style="left:412px;top:27px">Password:</label>
  <div class="field" style="left:517px;top:24px;width:240px">Enter Your Password</div>
  <span class="forgot">Forgot your password?</span>
  <div class="submit">
    <svg width="11" height="13" viewBox="0 0 11 13"><rect x="0" y="5.5" width="11" height="7.5" fill="#fff"/><path d="M2.5 5.5V4a3 3 0 016 0v1.5" fill="none" stroke="#fff" stroke-width="1.6"/></svg>
    LOG IN
  </div>
</section>

<section class="abs welcome">
  <h2 class="section-title"><strong>Welcome to</strong> Brindle Structures</h2>
  <p>Lorem ipsum dolor sit amet, consectetur adipiscing elit, sed do eiusmod tempor incididunt ut labore et dolore magna aliqua. Ut enim ad minim veniam, quis nostrud exercitation ullamco laboris nisi ut aliquip ex ea commodo consequat. Duis aute irure dolor in reprehenderit in voluptate velit esse cillum dolore eu fugiat nulla pariatur. Excepteur sint occaecat cupidatat non proident, sunt in culpa qui officia deserunt mollit anim id est laborum.Lorem ipsum dolor sit amet, consectetur adipiscing elit</p>
  <span class="btn-red">Read More</span>
</section>

<section class="abs feed">
  <h2 class="section-title"><strong>Latest</strong> Feed</h2>
  <span class="view-all">View All</span>
  <article class="feed-item">
    <div class="feed-thumb" role="img" aria-label="Two-storey family house with a front lawn" style="background:linear-gradient(180deg,#b9c7d3 0%,#8a6c58 55%,#5d7a45 100%)"></div>
    <div><time>12/08/2015</time><h3>Lorem Ipsum Dolor Sit</h3><p>Lorem ipsum dolor sit amet, consectetur adipiscing elit, sed do eiusmod tempor incididunt ut labore</p></div>
  </article>
  <article class="feed-item">
    <div class="feed-thumb" role="img" aria-label="White suburban house behind green trees" style="background:linear-gradient(180deg,#9fbfd9 0%,#dcdcd6 50%,#4f7a3a 100%)"></div>
    <div><time>12/08/2015</time><h3>Lorem Ipsum Dolor Sit</h3><p>Lorem ipsum dolor sit amet, consectetur adipiscing elit, sed do eiusmod tempor incididunt ut labore</p></div>
  </article>
</section>

<section class="abs projects">
  <div class="tile" role="img" aria-label="Hand passing house keys in front of a home, under a blue tint" style="left:48px;top:78px;width:677px;height:510px;background:linear-gradient(135deg,#4aa6d6 0%,#2a8ccb 55%,#1f7fbf 100%)">
    <h2>Consectetur Adipiscing Elit 1</h2>
    <p>Lorem ipsum dolor sit amet, consectetur adipiscing elit, sed do eiusmod tempor incididunt ut labore et dolore magna aliqua. Ut enim ad minim veniam</p>
    <span class="btn-red">Read More</span>
  </div>
  <div class="tile" role="img" aria-label="House with a for sale sign in the front yard" style="left:730px;top:78px;width:422px;height:252px;background:linear-gradient(135deg,#8a8676 0%,#6a6a60 50%,#7a3c34 100%)">
    <h2>Consectetur<br>Adipiscing Elit 2</h2>
  </div>
  <div class="tile" role="img" aria-label="Single-storey brick house with tiled roof and garden" style="left:730px;top:335px;width:422px;height:253px;background:linear-gradient(180deg,#a9c6e0 0%,#8f7f6b 50%,#4e7a36 100%)">
    <h2>Consectetur<br>Adipiscing Elit 3</h2>
  </div>
  <div class="tile" role="img" aria-label="Large brick house with double garage" style="left:48px;top:591px;width:549px;height:288px;background:linear-gradient(180deg,#7f8a86 0%,#5d4b40 55%,#4a4a42 100%)">
    <h2>Consectetur Adipiscing Elit 4</h2>
  </div>
  <div class="tile" role="img" aria-label="Hand holding a small model house with an orange roof" style="left:602px;top:591px;width:550px;height:288px;background:linear-gradient(135deg,#c9c7c2 0%,#a9a49c 50%,#c46a3a 100%)">
    <h2>Consectetur Adipiscing Elit 5</h2>
  </div>
</section>

<section class="abs partners">
  <div class="partner" style="left:247px;background:#f6e4e2"><i></i></div>
  <div class="partner" style="left:626px;background:#ee8a43"><i></i></div>
</section>

<section class="abs contact">
  <div class="contact-item" style="left:92px;top:30px">
    <span class="icon-box"><svg width="16" height="16" viewBox="0 0 24 24"><path fill="#d32f27" d="M6.6 10.8a15 15 0 006.6 6.6l2.2-2.2c.3-.3.7-.4 1-.2 1.1.4 2.3.6 3.6.6.6 0 1 .4 1 1V20c0 .6-.4 1-1 1A17 17 0 013 4c0-.6.4-1 1-1h3.5c.6 0 1 .4 1 1 0 1.3.2 2.5.6 3.6.1.3 0 .7-.2 1z"/></svg></span>
    123.456.7890
  </div>
  <div class="contact-item" style="left:422px;top:30px">
    <span class="icon-box"><svg width="16" height="14" viewBox="0 0 16 14"><rect x="0" y="4" width="16" height="10" fill="#d32f27"/><rect x="5" y="1" width="6" height="4" fill="none" stroke="#d32f27" stroke-width="1.6"/></svg></span>
    123.456.7890
  </div>
  <div class="contact-item" style="left:770px;top:30px">
    <span class="icon-box"><svg width="14" height="12" viewBox="0 0 14 12"><rect x=".7" y=".7" width="12.6" height="10.6" fill="none" stroke="#d32f27" stroke-width="1.4"/><path d="M1 1l6 5 6-5" fill="none" stroke="#d32f27" stroke-width="1.4"/></svg></span>
    info@companyname.com
  </div>
  <div class="contact-item small" style="left:92px;top:86px">
    <span class="icon-box"><svg width="12" height="16" viewBox="0 0 12 16"><path fill="#d32f27" d="M6 0a6 6 0 00-6 6c0 4.5 6 10 6 10s6-5.5 6-10a6 6 0 00-6-6zm0 8.5A2.5 2.5 0 116 3.5a2.5 2.5 0 010 5z"/></svg></span>
    Address Line1, Address line2, -123456, Country
  </div>
</section>

<footer class="abs footer">
  <p class="copy">All Right Reserved. Copyright ©2015 Brindle Structures</p>
  <div class="social"><span style="background:#fff"></span><span style="background:#fff"></span><span style="background:#fff"></span></div>
</footer>

</body>
</html>
```